Nieuwe slogan Quillbasket
Quillbasket is op zoek naar een Engelse, catchy slogan. De boodschap die we willen geven, is dat Quillbasket alleen overzicht geeft aan de beste dagaanbiedingen online. We verzamelen niet zomaar alle deals en stoppen die vervolgens in een chaotisch overzicht zoals onze concurrenten dat doen. Daardoor hoeven zij niet eindeloos naar beneden te scrollen om deals te checken.
De verkorte boodschap is dus: It's only a (true) bargain once Quillbasket has it. Belangrijk is dat de slogan catchy, duidelijk en niet te lang is.

```html
<!DOCTYPE html>
<html lang="en">
<head>
<meta charset="utf-8">
<title>Quillbasket slogan</title>
<link rel="stylesheet" href="https://fonts.googleapis.com/css2?family=Cousine&display=swap">
<style>
  :root {
    --paper: #ffffff;
    --ink: #111111;
  }
  html, body {
    margin: 0;
    padding: 0;
    overflow: hidden;
    background: var(--paper);
  }
  .canvas {
    position: relative;
    width: 1200px;
    height: 900px;
    background: var(--paper);
    overflow: hidden;
  }
  .slogan {
    position: absolute;
    left: 0;
    width: 1200px;
    margin: 0;
    text-align: center;
    font-family: "Cousine", "Liberation Mono", monospace;
    font-weight: 400;
    line-height: 1;
    color: var(--ink);
    box-sizing: border-box;
    white-space: nowrap;
  }
  .slogan-line {
    top: 347px;
    font-size: 62px;
    letter-spacing: 0.3em;
    padding-left: 0.3em;
    transform: translateX(-7px);
  }
  .slogan-brand {
    top: 440px;
    font-size: 26px;
    letter-spacing: 0.5em;
    padding-left: 0.5em;
    transform: translateX(-7px);
  }
</style>
</head>
<body>
  <main class="canvas">
    <h1 class="slogan slogan-line">TRUE BARGAINS ONLY</h1>
    <p class="slogan slogan-brand">QUILLBASKET</p>
  </main>
</body>
</html>
```